Corporate Identity Project for Veteran Transition Company

I am launching a company, Pathora.net. My tagline is:

Helping Veterans find great careers. Helping companies tap extra-ordinary talent.

This is my immediate need:
1. Stationary design that will appeal to both veterans and hiring companies.
2. Matching business card.

Next:
Ideally, I would like to hire someone who can also help me put together power-point presentations, or at least a template, of the same look and feel.

Extra credit: I already have a logo. I like it but could be persuaded to go with something else. If the winning designer, and only the winning designer, comes up with a better logo, I will pay a for it but don't want that to be what this is about.

More about the company:

Pathora's purpose is to help transitioning veterans find great jobs while helping companies tap the leadership skills, adaptability, and ability to work as team that defines veterans.

We do this by first helping veterans asses their individual strengths, interests, and transferrable skills. Next we help them map these to private sector career paths and teach them how to market themselves. In addition, we work with companies to onboard their veterans by offering a "Open Horizon Kickoff Workshop" to help vets succeed in civilian job cultures.

Our goal is create a scalable web based solution for all of our services so that we can cost efficiently serve the thousands of returning vets who are both geographically dispersed.

From a design stand point, I'm looking for something that will be professional enough to show CEO's of major companies as they will be our initial sponsors. It needs to look professional. While I am hoping you can help me with design and color palette etc. I do not want my design to look like it wears combat boots. i.e, no camouflage colors or military symbols.
Updates

Reason: First time user error :)

As the designs are coming in, a couple preferences that I seem to be developing and want to pass on to save everyone time:

1.  I like squared biz card edges vs. rounded.  Don't worry if your submission has rounded, I can visualize everything else just fine.
2.  I prefer a colored back of the card vs. a blank or white backing.

Thanks

Please keep in mind that I need the design to be able to work on both a business card and ppt template.

Excellent submissions so far.  I've just gone through them all and am going to eliminate several that simply don't fit into the criteria I updated earlier:

1.  Squared edges only
2.  Tag line must be on the front of the business card.

I will write what I want on the back in a couple of minutes.  

Thank you,

Tomas

Target Market(s)

CEOs, Heads of Human Resources at Meridian 300 companies.

Industry/Entity Type

Leadership

Requirements
Must have
• Must be able to use in ppt presentations so the company's look and feel is consistent.

On the back I'd like a Venn diagram similar to my second attachment. A central belief is that great jobs are all about finding something you are passionate about, inherantly good at doing, brings values to others, while allowing you to work in culture in which you can thrive.

Biz card info:

1. Logo
2. Tomas Lindqvist
3. Founder (below or by my name)
4. Phone number
5. Email: tomas.lindqvist@pathora.net
Note: Let's leave web address off until i'm ready to re-lanch the site.
Nice to have
• I am new to "Pixel Forum" so bear with me in using their technology. I would prefer to have two-way feedback so I don't waste your time while improving the odds of getting this exactly right so please do not hesitate to reach out.
Should not have
• No use of red-white-and blue or military motifs. While I aplaud the many not-for-profits out there helping vets, that apeal to "giving vets something back," I'm trying to come at this from a business proposition angle:

Vets have some terrific skills that businesses can want. They are just missing each other in the translation in getting hired and the help djusting to the new culture. That's where we come in!

```html
<!DOCTYPE html>
<html lang="en">
<head>
<meta charset="utf-8">
<title>Pathora Envelope</title>
<link rel="stylesheet" href="https://fonts.googleapis.com/css2?family=Tinos:wght@400;700&display=swap">
<style>
  :root {
    --backdrop: #3a3023;
    --paper: #f1f1f0;
    --navy: #1e3468;
    --ink: #2a2a2a;
    --rule: #3a3a3a;
  }
  * { margin: 0; padding: 0; box-sizing: border-box; }
  html, body {
    width: 1200px;
    height: 720px;
    overflow: hidden;
    background: var(--backdrop);
  }
  .canvas {
    position: relative;
    width: 1200px;
    height: 720px;
  }
  .envelope {
    position: absolute;
    background: var(--paper);
    box-shadow: 0 6px 18px rgba(0,0,0,0.45);
  }
  .envelope-back {
    left: 450px;
    top: 80px;
    width: 620px;
    height: 330px;
  }
  .flap-band {
    position: absolute;
    left: 0;
    top: 0;
    width: 100%;
    height: 30px;
    background: var(--navy);
    clip-path: polygon(0 0, 100% 0, 98% 100%, 2% 100%);
  }
  .envelope-front {
    left: 150px;
    top: 240px;
    width: 760px;
    height: 410px;
    font-family: "Tinos", "Times New Roman", serif;
  }
  .letterhead {
    position: absolute;
    left: 46px;
    top: 40px;
    display: flex;
    align-items: center;
  }
  .brand-name {
    color: var(--ink);
    font-size: 32px;
    font-weight: 400;
    line-height: 1;
    width: 124px;
  }
  .divider {
    width: 1px;
    height: 60px;
    background: var(--rule);
    margin: 0 14px 0 22px;
  }
  .return-address {
    font-style: normal;
    color: var(--ink);
    font-size: 12.5px;
    line-height: 1.3;
  }
  .return-address .company {
    font-weight: 700;
  }
  .web {
    display: flex;
    align-items: center;
    gap: 8px;
    margin-top: 3px;
    letter-spacing: 1.5px;
    font-weight: 700;
    font-size: 11.5px;
  }
  .web svg { display: block; }
</style>
</head>
<body>
  <main class="canvas">
    <div class="envelope envelope-back">
      <div class="flap-band"></div>
    </div>

    <div class="envelope envelope-front">
      <header class="letterhead">
        <div class="brand-name">Pathora</div>
        <div class="divider"></div>
        <address class="return-address">
          <div class="company">Pathora</div>
          <div>2480 Alder Crest Blvd.</div>
          <div>Suite 310, Lakeview, CA 90412</div>
          <div class="web">
            <svg width="8" height="11" viewBox="0 0 8 11" aria-hidden="true">
              <rect x="0.75" y="0.75" width="6.5" height="9.5" rx="3.25" fill="none" stroke="#1e3468" stroke-width="1.2"/>
              <line x1="4" y1="2.2" x2="4" y2="4.2" stroke="#1e3468" stroke-width="1.2"/>
            </svg>
            <span>www.pathora.net</span>
          </div>
        </address>
      </header>
    </div>
  </main>
</body>
</html>
```